Dance School poster for end of year dance concert for mainly young girls.

We need an A3 portrait poster for our end of year concert.
Designs are attached of posters from previous 2 years as a reference only.
The theme of our concert this year is "Let's Dance" which we want to convey a general feel of energy & fun with dance.
Dance styles in the concert include Jazz & Hip Hop.
Bright colors are preferred in the design.

Target Market(s)

The concert is attended by several hundred family & friends

Industry/Entity Type

Dance Studio

Requirements
Must have
• Must have
• Let's Dance
• BRK logo (file supplied)
• 'The Maribel Crowe Dancers' (font is Mistral)
• Date of the concert: Saturday 14th November 2015
• Pellow Theatre, Saint Fenwick College Dalebrook
Nice to have
• We like clean design with no cluttered imagery.

```html
<!DOCTYPE html>
<html lang="en">
<head>
<meta charset="utf-8">
<title>Let's Dance – The Maribel Crowe Dancers</title>
<link rel="stylesheet" href="https://fonts.googleapis.com/css2?family=Bebas+Neue&family=Kaushan+Script&family=Special+Elite&display=swap">
<style>
  :root {
    --peach: #f7c89e;
    --blush: #e9b7b4;
    --lavender: #c7a2d9;
    --white: #ffffff;
    --ink: #1e1a22;
    --plum: #6e4a86;
    --dancer-warm: #f29a6a;
    --dancer-cool: #9d8fc4;
    --dancer-lime: #c6dc84;
  }
  html, body {
    margin: 0;
    padding: 0;
    overflow: hidden;
  }
  .poster {
    position: relative;
    width: 849px;
    height: 1200px;
    overflow: hidden;
    background: linear-gradient(180deg, var(--peach) 0%, var(--blush) 50%, var(--lavender) 100%);
    font-family: "Special Elite", monospace;
  }
  .school-name {
    position: absolute;
    top: 30px;
    left: 0;
    width: 849px;
    text-align: center;
    margin: 0;
    font-family: "Kaushan Script", cursive;
    font-weight: 400;
    font-size: 42px;
    color: var(--ink);
  }
  .headline { margin: 0; }
  .headline-row {
    position: absolute;
    left: 30px;
    margin: 0;
    font-family: "Bebas Neue", sans-serif;
    font-weight: 400;
    font-size: 390px;
    line-height: 1;
    letter-spacing: 14px;
    color: var(--white);
    opacity: 0.95;
    z-index: 2;
  }
  .row-let  { top: 90px; }
  .row-s    { top: 370px; }
  .row-dan  { top: 610px; }
  .row-ce   { top: 880px; }

  .dancer {
    position: absolute;
    border-radius: 48% 52% 40% 60% / 55% 45% 55% 45%;
    z-index: 1;
  }
  .dancer-leap   { left: 600px; top: 70px;  width: 220px; height: 240px; background: linear-gradient(160deg, var(--dancer-cool), transparent); opacity: .75; }
  .dancer-turn   { left: 360px; top: 290px; width: 200px; height: 270px; background: linear-gradient(180deg, var(--dancer-warm), var(--dancer-cool)); opacity: .55; }
  .dancer-jump   { left: 610px; top: 650px; width: 190px; height: 170px; background: linear-gradient(135deg, var(--dancer-lime), var(--dancer-cool)); opacity: .8; }
  .dancer-reach  { left: 400px; top: 800px; width: 180px; height: 400px; background: linear-gradient(180deg, var(--dancer-warm), var(--dancer-cool)); opacity: .8; z-index: 3; }

  .event-date {
    position: absolute;
    left: 395px;
    top: 450px;
    margin: 0;
    font-size: 56px;
    line-height: 1.05;
    color: var(--plum);
    z-index: 4;
  }
  .event-date span { display: block; }
  .date-day { margin-left: 0; }
  .date-month { margin-left: -10px; }
  .date-month sup { font-size: 26px; }
  .date-year { margin-left: 110px; font-size: 66px; }

  .client-mark {
    position: absolute;
    left: 120px;
    top: 1000px;
    width: 96px;
    height: 96px;
    border-radius: 50%;
    border: 4px solid var(--white);
    display: flex;
    align-items: center;
    justify-content: center;
    font-size: 30px;
    color: var(--white);
    z-index: 4;
  }

  .venue {
    position: absolute;
    left: 630px;
    top: 960px;
    width: 200px;
    color: var(--ink);
    z-index: 4;
  }
  .venue-pin { display: block; width: 30px; height: 44px; margin-bottom: 14px; }
  .venue-name { margin: 0; font-size: 32px; line-height: 1.1; }
  .venue-place { margin: 14px 0 0; font-size: 17px; line-height: 1.5; }
</style>
</head>
<body>
<main class="poster">
  <p class="school-name">The Maribel Crowe Dancers</p>

  <div class="dancer dancer-leap" role="img" aria-label="Silhouette of a dancer leaping"></div>
  <div class="dancer dancer-turn" role="img" aria-label="Silhouette of a dancer turning"></div>
  <div class="dancer dancer-jump" role="img" aria-label="Silhouette of a hip hop dancer jumping"></div>
  <div class="dancer dancer-reach" role="img" aria-label="Silhouette of a dancer reaching upward"></div>

  <h1 class="headline" aria-label="Let's Dance">
    <span class="headline-row row-let">LET</span>
    <span class="headline-row row-s">'S</span>
    <span class="headline-row row-dan">DAN</span>
    <span class="headline-row row-ce">CE</span>
  </h1>

  <p class="event-date">
    <span class="date-day">Saturday</span>
    <span class="date-month">14<sup>th</sup> November</span>
    <span class="date-year">2015</span>
  </p>

  <div class="client-mark">BRK</div>

  <address class="venue">
    <svg class="venue-pin" viewBox="0 0 30 44" aria-hidden="true">
      <path d="M15 2C7.8 2 2 7.8 2 15c0 9.5 13 27 13 27s13-17.5 13-27C28 7.8 22.2 2 15 2z" fill="#ffffff"/>
      <circle cx="15" cy="15" r="5" fill="#e9b7b4"/>
    </svg>
    <p class="venue-name">Pellow<br>Theatre</p>
    <p class="venue-place">Saint Fenwick College<br>Dalebrook</p>
  </address>
</main>
</body>
</html>
```